a residential cleaning service needs a website

We need a website for our faith based residential cleaning service, we are called MARGOT'S CLEANING SERVICE. We want a website that is clean looking both for mobile version and desktop. We want to convey cleanliness and trust to our clients. The color scheme should go in hand with the colors of the LOGO. We would like an about page, statement of faith page, services page and also a page for a booking module that our CRM has provided for us to being able to code and dress said module is important. The website not only needs to market to new customers and convey our service but also be easy to use for existing clients to schedule cleanings and services.
Industry/Entity Type
Cleaning Service
Coding
Coded - Design and coding required
Number of Pages Required
4 page
Requirements
Must have
- About page
Statement of Faith page
services page
booking and login page

```html
<!DOCTYPE html>
<html lang="en">
<head>
<meta charset="utf-8">
<title>Margot's Cleaning Service</title>
<link href="https://fonts.googleapis.com/css2?family=Cinzel:wght@500;600;700&family=Fira+Sans:wght@500;600&family=Poppins:wght@300;400;500;600&display=swap" rel="stylesheet">
<style>
:root{
  --blue:#2350a3;
  --blue-dark:#1e479a;
  --ink:#2a2a2a;
  --muted:#6b6b6b;
  --pale:#f3f4f8;
  --line:#e3e6ee;
  --white:#ffffff;
}
*{box-sizing:border-box;margin:0;padding:0}
html,body{width:1200px;height:3992px;overflow:hidden}
body{position:relative;background:var(--white);font-family:"Poppins",sans-serif;color:var(--ink)}
.abs{position:absolute}
.serif{font-family:"Cinzel",serif}
.photo{position:absolute;overflow:hidden}

/* nav */
.site-nav{position:absolute;left:0;top:0;width:1200px;height:67px;background:var(--white);z-index:5}
.nav-link{position:absolute;top:26px;font-size:11.5px;color:var(--ink);white-space:nowrap}
.nav-link.active{color:var(--blue)}
.nav-link.active::before{content:"";display:inline-block;width:6px;height:6px;border-radius:50%;background:var(--blue);margin-right:7px;vertical-align:2px}
.nav-login{position:absolute;left:839px;top:25px;font-family:"Cinzel",serif;font-weight:700;font-size:14px;color:var(--blue)}
.nav-book{position:absolute;left:904px;top:17px;width:135px;height:37px;background:var(--blue);color:#fff;border-radius:3px;font-family:"Cinzel",serif;font-size:14px;display:flex;align-items:center;justify-content:center;letter-spacing:.5px}
.brand-badge{position:absolute;left:161px;top:-18px;width:152px;height:152px;border-radius:50%;background:var(--white);z-index:6;display:flex;align-items:center;justify-content:center;text-align:center;padding:0 18px}
.brand-name{font-family:"Cinzel",serif;font-weight:700;color:var(--blue);font-size:13px;line-height:1.25}

/* hero */
.hero{position:absolute;left:0;top:67px;width:1200px;height:646px;overflow:hidden}
.hero-photo{left:0;top:0;width:1200px;height:646px;background:linear-gradient(100deg,#c9cfd6 0%,#e4e7ea 40%,#eef0f2 70%,#d2d7dd 100%)}
.hero-title{position:absolute;left:110px;top:140px;width:405px;text-align:center;font-family:"Fira Sans",sans-serif;font-weight:600;font-size:46px;line-height:52px;color:#fff}
.hero-sub{position:absolute;left:110px;top:255px;width:405px;text-align:center;font-size:17px;color:#fff}
.hero-btn{position:absolute;left:230px;top:300px;width:136px;height:41px;border:1.5px solid #fff;border-radius:4px;color:#fff;font-family:"Cinzel",serif;font-size:15px;display:flex;align-items:center;justify-content:center}
.hero-dots{position:absolute;left:547px;top:611px;display:flex;gap:9px}
.hero-dots span{width:14px;height:14px;border-radius:50%;border:1.5px solid #fff}
.hero-dots .on{background:var(--blue);border-color:var(--blue)}

/* welcome */
.eyebrow{font-family:"Cinzel",serif;font-size:16px;color:var(--ink);letter-spacing:.5px}
.section-title{font-family:"Cinzel",serif;font-weight:600;color:var(--blue)}
.body-copy{font-size:11.5px;line-height:21px;color:var(--muted)}
.btn-solid{position:absolute;background:var(--blue);color:#fff;border-radius:3px;font-family:"Cinzel",serif;font-size:15px;display:flex;align-items:center;justify-content:center;letter-spacing:.5px}

/* services */
.service-icon{position:absolute;width:74px;height:74px;border-radius:50%;background:var(--blue);display:flex;align-items:center;justify-content:center}
.service-name{position:absolute;font-family:"Cinzel",serif;font-size:15px;color:var(--blue);letter-spacing:.5px}
.service-desc{position:absolute;font-size:11.5px;line-height:20px;color:var(--muted)}

/* faith */
.faith{position:absolute;left:0;top:1925px;width:1200px;height:470px;background:var(--blue-dark)}
.faith .body-copy{color:#fff}
.btn-outline{position:absolute;border:1.5px solid #fff;border-radius:20px;color:#fff;font-family:"Cinzel",serif;font-size:15px;display:flex;align-items:center;justify-content:center}

/* why */
.why-card{position:absolute;width:262px;text-align:center}
.why-card .photo{position:relative;width:262px;height:186px}
.why-title{font-family:"Cinzel",serif;font-size:15px;line-height:22px;color:var(--blue);margin-top:42px;letter-spacing:.5px}
.why-desc{font-size:10.5px;line-height:20px;color:var(--muted);margin:12px -10px 0}
.why-more{display:inline-block;margin-top:16px;font-family:"Cinzel",serif;font-size:11px;font-weight:700;color:var(--blue);text-decoration:underline}
.why-more::after{content:"";display:inline-block;margin-left:6px;border-left:6px solid var(--blue);border-top:4px solid transparent;border-bottom:4px solid transparent}

/* booking */
.form-card{position:absolute;left:284px;top:3154px;width:415px;height:388px;background:#fff;box-shadow:0 2px 18px rgba(0,0,0,.07)}
.field{position:absolute;left:37px;width:335px;height:37px;border:1px solid var(--line);font-size:11px;color:var(--muted);padding:11px 13px}

/* contact band */
.contact-band{position:absolute;left:0;top:3632px;width:1200px;height:197px;background:var(--blue-dark);color:#fff}
.contact-col{position:absolute;top:0;width:280px;text-align:center}
.contact-col svg{position:absolute;left:122px;top:55px}
.contact-label{position:absolute;top:103px;width:280px;font-family:"Cinzel",serif;font-size:15px;letter-spacing:.5px}
.contact-value{position:absolute;top:131px;width:280px;font-size:12.5px}
.divider{position:absolute;top:58px;width:1px;height:100px;background:rgba(255,255,255,.2)}

/* footer */
.footer-links{position:absolute;left:396px;top:3890px;font-size:11.5px;color:var(--muted)}
.footer-links span{margin:0 6px}
.copyright{position:absolute;left:446px;top:3918px;font-size:11px;color:var(--muted)}
.copyright b{font-weight:400;color:var(--blue)}
.social{position:absolute;top:3887px;width:34px;height:34px;border-radius:50%}
</style>
</head>
<body>

<!-- navigation -->
<header class="site-nav">
  <nav>
    <span class="nav-link active" style="left:438px">Home</span>
    <span class="nav-link" style="left:509px">About</span>
    <span class="nav-link" style="left:561px">Statement of Faith</span>
    <span class="nav-link" style="left:686px">Services</span>
    <span class="nav-link" style="left:754px">Contact Us</span>
  </nav>
  <span class="nav-login">LOGIN</span>
  <span class="nav-book">BOOK NOW</span>
</header>
<div class="brand-badge"><span class="brand-name">MARGOT'S CLEANING SERVICE</span></div>

<!-- hero -->
<section class="hero">
  <div class="photo hero-photo" role="img" aria-label="Bright modern room with a cleaner operating a floor scrubbing machine, potted plants by the window"></div>
  <svg class="abs" style="left:0;top:0" width="1200" height="646">
    <circle cx="248" cy="120" r="320" fill="#2350a3"/>
    <circle cx="1200" cy="545" r="47" fill="#2350a3"/>
  </svg>
  <h1 class="hero-title">Cleaning With Higher Purpose</h1>
  <p class="hero-sub">Margot's Cleaning Service</p>
  <span class="hero-btn">BOOK NOW</span>
  <div class="hero-dots"><span></span><span></span><span></span><span class="on"></span><span></span></div>
</section>

<!-- welcome -->
<section>
  <svg class="abs" style="left:220px;top:797px" width="330" height="330">
    <circle cx="164" cy="164" r="160" fill="none" stroke="#2350a3" stroke-width="3"/>
  </svg>
  <div class="photo" style="left:238px;top:815px;width:293px;height:293px;border-radius:50%;background:radial-gradient(circle at 40% 40%,#f4f6f7,#cfd6dc)" role="img" aria-label="Cleaner in a blue apron holding a mop in a bright living room"></div>
  <div class="photo" style="left:295px;top:1150px;width:80px;height:22px;background:linear-gradient(#8ea7d6,#3d62ad);border-radius:2px" role="img" aria-label="Flat mop head"></div>
  <p class="eyebrow abs" style="left:634px;top:805px">WELCOME TO</p>
  <h2 class="section-title abs" style="left:632px;top:832px;font-size:34px">MARGOT'S CLEANING</h2>
  <p class="body-copy abs" style="left:635px;top:886px;width:345px">Margot's Cleaning Service is a faith based cleaning business founded in middle Tennessee over 19 years ago. Fueled by great work and word of mouth, a part time source of income to a mother of 4 changed and grew by into a full time job.</p>
  <p class="body-copy abs" style="left:635px;top:1003px;width:345px">Over the years Margot's Cleaning Service has developed its cleaning process into a methodical approach where attention to detail and a continual striving for excellence presents itself in everything we do.</p>
  <span class="btn-solid" style="left:637px;top:1105px;width:141px;height:41px">LEARN MORE</span>
</section>

<!-- services -->
<section>
  <svg class="abs" style="left:0;top:1195px" width="1200" height="730">
    <path d="M0 40 C150 0 300 20 420 80 C520 130 600 200 760 190 C900 180 1000 120 1200 100 L1200 730 L0 730 Z" fill="#f4f5f8"/>
    <path d="M0 40 C150 0 300 20 420 80" fill="none" stroke="#eceef3" stroke-width="30"/>
  </svg>
  <h2 class="section-title abs" style="left:0;top:1252px;width:1200px;text-align:center;font-size:37px">OUR SERVICES</h2>

  <div class="service-icon" style="left:561px;top:1324px">
    <svg width="40" height="40" viewBox="0 0 40 40" fill="none" stroke="#fff" stroke-width="1.8"><circle cx="14" cy="18" r="9"/><path d="M14 13v5l3 2"/><path d="M30 6v16M25 22h10l2 12H23z"/></svg>
  </div>
  <p class="service-name" style="left:0;top:1414px;width:1200px;text-align:center">ONE TIME CLEANING</p>
  <p class="service-desc" style="left:460px;top:1440px;width:280px;text-align:center">Planning a party, hosting the in-laws, or just too busy to clean this week?</p>

  <div class="service-icon" style="left:343px;top:1533px">
    <svg width="40" height="40" viewBox="0 0 40 40" fill="none" stroke="#fff" stroke-width="1.8"><path d="M6 20 20 7l14 13M10 17v16h20V17"/><circle cx="20" cy="23" r="4"/><path d="M20 27v6"/></svg>
  </div>
  <p class="service-name" style="left:150px;top:1623px;width:250px;text-align:right">MOVE IN – MOVE OUT</p>
  <p class="service-desc" style="left:160px;top:1650px;width:240px;text-align:right">We understand that moving is a daunting process and we are delighted to offer services if that means.</p>

  <div class="service-icon" style="left:788px;top:1533px">
    <svg width="40" height="40" viewBox="0 0 40 40" fill="none" stroke="#fff" stroke-width="1.8"><rect x="8" y="14" width="24" height="18"/><path d="M12 14V8h16v6M12 20h6M12 25h10M26 19v8"/></svg>
  </div>

  <svg class="abs" style="left:425px;top:1510px" width="350" height="350">
    <path d="M175 8 A167 167 0 0 0 18 230" fill="none" stroke="#4a4a4a" stroke-width="6"/>
    <path d="M190 12 A163 163 0 0 1 290 300" fill="none" stroke="#2350a3" stroke-width="6"/>
    <path d="M275 318 A167 167 0 0 1 120 338" fill="none" stroke="#4a4a4a" stroke-width="5"/>
  </svg>
  <div class="photo" style="left:460px;top:1545px;width:275px;height:275px;border-radius:50%;background:radial-gradient(circle at 50% 40%,#f5f6f7,#cfd5db)" role="img" aria-label="Bright room with a floor scrubbing machine and exercise ball"></div>
  <div class="photo" style="left:430px;top:1690px;width:170px;height:152px;border-radius:20px 20px 30px 30px;background:linear-gradient(160deg,#3a7fd6,#1b56b5 60%,#e8b923)" role="img" aria-label="Blue bucket of cleaning supplies with yellow gloves and a brush"></div>
</section>

<!-- statement of faith -->
<section class="faith">
  <div class="photo" style="left:279px;top:31px;width:264px;height:439px;border-radius:110px 110px 0 0;background:linear-gradient(180deg,#e8c48c 0%,#f1d6b5 30%,#7aa8e0 55%,#d8e4f5 100%)" role="img" aria-label="Smiling cleaner in an apron and gloves holding a spray bottle"></div>
  <h2 class="serif abs" style="left:642px;top:70px;width:320px;font-size:37px;line-height:42px;font-weight:600;color:#fff">STATEMENT OF FAITH</h2>
  <p class="body-copy abs" style="left:642px;top:162px;width:345px;font-size:11.5px">As a faith based business Margot's Cleaning Service clings to <b>Colossians 3:23 " And whatsoever ye do, do it heartily as to The Lord and not unto men."</b></p>
  <p class="body-copy abs" style="left:642px;top:238px;width:345px;font-size:11.5px">Therefore every job that we do we as a business we pray that the job we perform is pleasing to God. Not only do we see every job as an opportunity to glorify God, but we see every client as a member of the family and look for opportunities to show love and be a light in a dark world.</p>
  <span class="btn-outline" style="left:642px;top:357px;width:136px;height:36px">BOOK NOW</span>
</section>

<!-- why choose us -->
<section>
  <h2 class="section-title abs" style="left:0;top:2490px;width:1200px;text-align:center;font-size:37px">WHY CHOOSE US ?</h2>
  <div class="why-card" style="left:180px;top:2570px">
    <div class="photo" style="background:linear-gradient(135deg,#9a8f86,#d9d2ca 50%,#c74141 80%,#3c70c8)" role="img" aria-label="Mop and bucket of cleaning supplies beside a sofa"></div>
    <p class="why-title">WE SUPPLY<br>EVERYTHING</p>
    <p class="why-desc">Margot's Cleaning Service provides all equipment and cleaning supplies needed to clean your home to the highest standards.</p>
    <span class="why-more">LEARN MORE</span>
  </div>
  <div class="why-card" style="left:468px;top:2570px">
    <div class="photo" style="background:linear-gradient(135deg,#e9ecef,#c9d0d6 50%,#5b8fd4 70%,#e3c33d)" role="img" aria-label="Cleaner vacuuming a bright living room"></div>
    <p class="why-title">HIGHLY TRAINED, &amp;<br>SCREENED EMPLOYEES</p>
    <p class="why-desc">Our professional house cleaners are held to very high standards not only in cleaning, but social performance as well.</p>
    <span class="why-more">LEARN MORE</span>
  </div>
  <div class="why-card" style="left:753px;top:2570px">
    <div class="photo" style="background:linear-gradient(135deg,#dfe6da,#f1ece6 45%,#c7474f 70%,#e7d04a)" role="img" aria-label="Smiling cleaner wiping a surface in a kitchen"></div>
    <p class="why-title">SURPRISINGLY<br>AFFORDABLE</p>
    <p class="why-desc">At Margot's Cleaning Service we are often able to offer our high quality cleaning services at lower cost than our big company competitors.</p>
    <span class="why-more">LEARN MORE</span>
  </div>
</section>

<!-- booking -->
<section>
  <div class="photo" style="left:660px;top:3000px;width:540px;height:632px;background:linear-gradient(90deg,#ffffff 0%,#f3f5f7 40%,#eceff2 100%)" role="img" aria-label="Soft faded view of a bright, clean living room"></div>
  <h2 class="section-title abs" style="left:284px;top:3030px;width:432px;text-align:center;font-size:37px;line-height:40px;font-weight:500">BOOK AN APPOINTMENT</h2>
  <p class="abs" style="left:284px;top:3111px;width:432px;text-align:center;font-size:12.5px;color:var(--ink)">If you have an any Question for Contact Us Today !</p>
  <form class="form-card">
    <div class="field" style="top:37px">Name *</div>
    <div class="field" style="top:86px">Email *</div>
    <div class="field" style="top:135px">Phone *</div>
    <div class="field" style="top:183px">Services *</div>
    <div class="field" style="top:231px;height:72px">Message *</div>
    <span class="btn-solid" style="left:161px;top:315px;width:110px;height:39px;font-size:14px">SUBMIT</span>
  </form>
  <div class="photo" style="left:710px;top:3310px;width:267px;height:255px;border-radius:30px 30px 40px 40px;background:linear-gradient(160deg,#3a80d8,#1b55b4 60%,#e8b923)" role="img" aria-label="Blue bucket of cleaning bottles with yellow gloves and a scrub brush"></div>
</section>

<!-- contact band -->
<section class="contact-band">
  <div class="contact-col" style="left:164px">
    <svg width="36" height="36" viewBox="0 0 24 24" fill="#fff"><path d="M6.6 10.8a15.1 15.1 0 0 0 6.6 6.6l2.2-2.2a1 1 0 0 1 1-.25 11.4 11.4 0 0 0 3.6.57 1 1 0 0 1 1 1V20a1 1 0 0 1-1 1A17 17 0 0 1 3 4a1 1 0 0 1 1-1h3.5a1 1 0 0 1 1 1c0 1.25.2 2.46.57 3.6a1 1 0 0 1-.25 1z"/></svg>
    <p class="contact-label">PHONE:</p>
    <p class="contact-value">123 456 7890</p>
  </div>
  <div class="divider" style="left:465px"></div>
  <div class="contact-col" style="left:458px">
    <svg width="36" height="36" viewBox="0 0 24 24" fill="#fff"><path d="M12 2a7 7 0 0 0-7 7c0 5.2 7 13 7 13s7-7.8 7-13a7 7 0 0 0-7-7zm0 9.5A2.5 2.5 0 1 1 12 6.5a2.5 2.5 0 0 1 0 5z"/></svg>
    <p class="contact-label">MARGOT'S CLEANING</p>
    <p class="contact-value">101 - Lorem ipsum simple text</p>
  </div>
  <div class="divider" style="left:741px"></div>
  <div class="contact-col" style="left:756px">
    <svg width="40" height="36" viewBox="0 0 24 20" fill="#fff"><path d="M2 2h20v3l-10 6L2 5z"/><path d="M2 7.5l10 6 10-6V18H2z"/></svg>
    <p class="contact-label">EMAIL US :</p>
    <p class="contact-value">info@margotscleaning.com</p>
  </div>
</section>

<!-- footer -->
<footer>
  <div class="abs" style="left:158px;top:3853px;width:100px;height:90px;display:flex;align-items:center;justify-content:center;text-align:center">
    <span class="brand-name" style="font-size:11px">MARGOT'S CLEANING SERVICE</span>
  </div>
  <p class="footer-links">Home<span>|</span>About<span>|</span>Statement of Faith<span>|</span>Services<span>|</span>Booking<span>|</span>Contact</p>
  <p class="copyright">©<b>MARGOT'S CLEANING SERVICE</b> -2020 All rights reserved.</p>
  <span class="social" style="left:924px;background:#1e3f86"></span>
  <span class="social" style="left:964px;background:#1da1f2"></span>
  <span class="social" style="left:1004px;background:#4a6a96"></span>
</footer>

</body>
</html>
```